craft brewery needs a 500ml beer bottle label

We need a beer bottle label for a new beer called 'Sunny Mango Drift NEIPA'
Its based on the movie Rink Kings.
We have come up with the name because the beer taste like tropical fruit juice.
So we wanted a tropical theme to the logo.
I have attached one of our old beer labels, but because this will go on larger bottles the dimensions will be -
height=9.75cm
Length= 19cm

I have also attached a rough drawing of what i want the layout of the label to look like, but would like some added material as i am not very creative.
I have also added some other labels which i like the designs of which could be added to this label.
Updates

Target Market(s)

young/ outdoors type/ active/ hipster

Industry/Entity Type

Movie

Colors
33a6d7
ffcf3e
faa54b
f37122
ffffff

Requirements
Must have
• Whats on the attached drawing.
• Copper hollow brewing logo which is on one of the attached files
Nice to have
• tropical style/ colourful/ artistic

```html
<!DOCTYPE html>
<html lang="en">
<head>
<meta charset="utf-8">
<title>Sunny Mango Drift NEIPA – Label</title>
<link rel="stylesheet" href="https://fonts.googleapis.com/css2?family=Kaushan+Script&family=Fira+Sans:ital,wght@0,700;1,700;1,800&display=swap">
<style>
  :root {
    --page: #f4f4f4;
    --sunset: #f37122;
    --sunset-deep: #e45d22;
    --sea: #86d9dd;
    --stripe: #1f5fae;
    --foam: #ffffff;
    --sand: #f2e6cb;
    --sun: #ffcf3e;
    --ink-blue: #1f5fae;
    --ink-orange: #ef5a24;
    --leaf: #1e8c3a;
    --zig-top: #f0623a;
    --zig-bottom: #3aa04a;
  }
  * { box-sizing: border-box; margin: 0; padding: 0; }
  html, body { width: 858px; height: 1200px; overflow: hidden; }
  body { background: var(--page); position: relative; }

  .label {
    position: absolute;
    left: 79px; top: 64px;
    width: 700px; height: 1072px;
    overflow: hidden;
    box-shadow: 0 6px 24px rgba(0,0,0,.12);
  }
  .label-scene { position: absolute; inset: 0; display: block; }

  .brand-mark {
    position: absolute;
    left: 308px; top: 172px;
    width: 220px; height: 220px;
    border-radius: 50%;
    background: var(--sun);
    display: flex; align-items: center; justify-content: center;
    text-align: center;
  }
  .brand-name {
    font-family: "Fira Sans", sans-serif;
    font-weight: 700;
    font-size: 34px;
    line-height: 1.05;
    color: var(--leaf);
    text-transform: uppercase;
  }

  .beer-title {
    position: absolute;
    left: 0; right: 0; top: 660px;
    text-align: center;
  }
  .beer-kicker {
    display: block;
    font-family: "Fira Sans", sans-serif;
    font-style: italic; font-weight: 700;
    font-size: 54px;
    color: var(--ink-orange);
    margin-left: 90px;
    line-height: 1;
  }
  .beer-name {
    display: block;
    font-family: "Kaushan Script", cursive;
    font-size: 150px;
    color: var(--ink-blue);
    line-height: 1;
    margin-top: -6px;
    margin-left: 40px;
  }
  .beer-style {
    display: block;
    font-family: "Fira Sans", sans-serif;
    font-style: italic; font-weight: 800;
    font-size: 72px;
    color: var(--ink-orange);
    letter-spacing: 1px;
    line-height: 1;
    margin-left: 210px;
    margin-top: -8px;
  }
</style>
</head>
<body>
  <section class="label">
    <svg class="label-scene" viewBox="0 0 700 1072" width="700" height="1072" aria-hidden="true">
      <rect class="sky" x="0" y="0" width="700" height="660" fill="var(--sunset)"/>
      <path class="sea" d="M0,455 C250,400 500,330 700,230 L700,640 L0,640 Z" fill="var(--sea)"/>
      <path class="sea-stripe" d="M0,371 C250,320 520,230 640,121 L680,121 C570,270 310,405 0,455 Z" fill="var(--stripe)"/>
      <path class="shoreline" d="M0,576 C250,540 500,530 700,556 L700,640 L0,640 Z" fill="var(--foam)"/>
      <path class="beach" d="M0,640 C250,600 500,592 700,613 L700,1072 L0,1072 Z" fill="var(--sand)"/>
    </svg>
    <svg class="label-scene" viewBox="0 0 700 1072" width="700" height="1072">
      <rect role="img" aria-label="Zigzag pattern band in orange, red and yellow" x="0" y="0" width="700" height="121" fill="var(--zig-top)"/>
      <rect role="img" aria-label="Palm leaf silhouettes in the sunset sky" x="0" y="130" width="260" height="230" fill="var(--sunset-deep)" opacity=".45"/>
      <rect role="img" aria-label="Palm tree illustration on the beach" x="170" y="440" width="175" height="300" rx="30" fill="var(--stripe)" opacity=".18"/>
      <rect role="img" aria-label="Zigzag pattern band in green and yellow" x="0" y="984" width="700" height="88" fill="var(--zig-bottom)"/>
    </svg>

    <div class="brand-mark">
      <span class="brand-name">Copper<br>Hollow<br>Brewing</span>
    </div>

    <h1 class="beer-title">
      <span class="beer-kicker">sunny mango</span>
      <span class="beer-name">drift!</span>
      <span class="beer-style">NEIPA</span>
    </h1>
  </section>
</body>
</html>
```